Business Card for innovative, tech/consultant company

We are specializing in bringing together Efficiency methodology and Technology for our Business customers. We would like an astonishing business Card that matches this idea.

Target Market(s)

Businesses of medium size or more

Industry/Entity Type

Business Consultant

Contact Information for Business Card

Name, Title, personal email, www, address, phone

Font styles to use
Sans Serif

Colors
3277b5

Requirements
Must have
• - innovative, efficient design
• - good readable
• - Colors must match our logo (blue and grey)
• - the attached font (is licensed by our Company) must be used (Syntax LT)
Should not have
• overloaded

```html
<!DOCTYPE html>
<html lang="en">
<head>
<meta charset="utf-8">
<title>Klarent Business Card</title>
<link rel="stylesheet" href="https://fonts.googleapis.com/css2?family=Open+Sans:wght@400;600;700&display=swap">
<style>
  :root {
    --page-bg: #e6e6e6;
    --card-white: #fbfbfb;
    --card-white-shade: #ececec;
    --brand-blue: #1aa3d6;
    --brand-grey: #9c9da1;
    --band-grey-dark: #8a8b8f;
    --band-grey-light: #a9aaae;
    --text-light: #ffffff;
    --icon-blue: #2a8fc8;
  }
  * { box-sizing: border-box; margin: 0; padding: 0; }
  html, body {
    width: 1200px;
    height: 780px;
    overflow: hidden;
    background: var(--page-bg);
    font-family: "Open Sans", Arial, sans-serif;
  }
  .business-card {
    position: absolute;
    left: 75px;
    top: 90px;
    width: 1050px;
    height: 600px;
    background: var(--card-white);
    box-shadow: 0 10px 30px rgba(0,0,0,0.18);
    overflow: hidden;
  }
  .name-area {
    position: absolute;
    left: 0; top: 0;
    width: 100%;
    height: 330px;
    background: linear-gradient(180deg, var(--card-white) 0%, var(--card-white-shade) 100%);
    display: flex;
    align-items: center;
    justify-content: center;
    padding-top: 20px;
  }
  .company-name {
    font-size: 170px;
    font-weight: 400;
    line-height: 1;
    letter-spacing: -2px;
    color: var(--brand-grey);
  }
  .accent-stripe {
    position: absolute;
    left: 0;
    top: 330px;
    width: 100%;
    height: 12px;
    background: var(--brand-blue);
  }
  .contact-band {
    position: absolute;
    left: 0;
    top: 342px;
    width: 100%;
    height: 258px;
    background: linear-gradient(90deg, var(--band-grey-dark) 0%, var(--band-grey-light) 55%, var(--band-grey-dark) 100%);
    display: flex;
    align-items: center;
    color: var(--text-light);
    padding: 0 60px 0 150px;
  }
  .person { width: 390px; }
  .person-name {
    font-size: 34px;
    font-weight: 700;
    line-height: 1.15;
  }
  .person-title {
    font-size: 25px;
    font-weight: 400;
    line-height: 1.2;
    margin-bottom: 6px;
  }
  .person-address {
    font-size: 27px;
    font-weight: 400;
    line-height: 1.25;
    font-style: normal;
  }
  .band-divider {
    width: 2px;
    height: 170px;
    background: rgba(255,255,255,0.75);
    margin: 0 40px 0 20px;
  }
  .contact-list { list-style: none; }
  .contact-item {
    display: flex;
    align-items: center;
    gap: 18px;
    font-size: 27px;
    line-height: 1.3;
    margin: 2px 0;
  }
  .contact-icon {
    width: 26px;
    height: 26px;
    flex: none;
  }
</style>
</head>
<body>
  <div class="business-card">
    <div class="name-area">
      <span class="company-name">Klarent</span>
    </div>
    <div class="accent-stripe"></div>
    <div class="contact-band">
      <div class="person">
        <p class="person-name">Employee Name</p>
        <p class="person-title">Managing Director</p>
        <address class="person-address">your address Rd.,<br>Suite 000, Roswell, USA</address>
      </div>
      <div class="band-divider"></div>
      <ul class="contact-list">
        <li class="contact-item">
          <svg class="contact-icon" viewBox="0 0 26 26" aria-hidden="true">
            <rect width="26" height="26" rx="3" fill="#fff"/>
            <rect x="8" y="4" width="10" height="18" rx="2" fill="none" stroke="var(--icon-blue)" stroke-width="2"/>
            <circle cx="13" cy="18.5" r="1.2" fill="var(--icon-blue)"/>
          </svg>
          <span>000.000.0000</span>
        </li>
        <li class="contact-item">
          <svg class="contact-icon" viewBox="0 0 26 26" aria-hidden="true">
            <rect width="26" height="26" rx="3" fill="#fff"/>
            <path d="M8 6 C6 8 7 13 10 16 C13 19 18 20 20 18 L17 15 L15 16.5 C13 15.5 10.5 13 9.5 11 L11 9 Z" fill="var(--icon-blue)"/>
          </svg>
          <span>000.000.0000</span>
        </li>
        <li class="contact-item">
          <svg class="contact-icon" viewBox="0 0 26 26" aria-hidden="true">
            <rect width="26" height="26" rx="3" fill="#fff"/>
            <rect x="5" y="7" width="16" height="12" fill="var(--icon-blue)"/>
            <path d="M5 7 L13 14 L21 7" fill="none" stroke="#fff" stroke-width="1.5"/>
          </svg>
          <span>info@youremail.com</span>
        </li>
        <li class="contact-item">
          <svg class="contact-icon" viewBox="0 0 26 26" aria-hidden="true">
            <rect width="26" height="26" rx="3" fill="#fff"/>
            <circle cx="13" cy="13" r="8" fill="none" stroke="var(--icon-blue)" stroke-width="1.6"/>
            <ellipse cx="13" cy="13" rx="3.5" ry="8" fill="none" stroke="var(--icon-blue)" stroke-width="1.4"/>
            <line x1="5" y1="13" x2="21" y2="13" stroke="var(--icon-blue)" stroke-width="1.4"/>
          </svg>
          <span>www.yourwebsite.com</span>
        </li>
      </ul>
    </div>
  </div>
</body>
</html>
```